New business stationairy

I need paper with header and footer and business cards.
I am a Ltd Company and my main field of expertise is QA/QC inspection in the Oil and Gas Industry. I will need all contact detail inserted and a footer with registration number and bank details etc

Industry/Entity Type

Business

```html
<!DOCTYPE html>
<html lang="en">
<head>
<meta charset="utf-8">
<title>Hartwell Inspection Services Ltd — Letterhead</title>
<link rel="stylesheet" href="https://fonts.googleapis.com/css2?family=Source+Sans+3:wght@700&family=Cabin:wght@400;500&display=swap">
<style>
  :root {
    --page-bg: #e6e6e6;
    --paper: #ffffff;
    --band: #a0f6fb;
    --ink: #2f5fdc;
    --rule: #3757d2;
    --art: #4f86d6;
  }
  html, body {
    margin: 0;
    width: 912px;
    height: 1200px;
    overflow: hidden;
    background: var(--page-bg);
  }
  .letterhead {
    position: absolute;
    left: 36px;
    top: 58px;
    width: 840px;
    height: 1084px;
    background: var(--paper);
    box-shadow: 0 2px 8px rgba(0,0,0,0.18);
    overflow: hidden;
  }
  .header-band {
    position: absolute;
    left: 0; top: 0;
    width: 840px; height: 170px;
    background: var(--band);
  }
  .art-pumpjack {
    position: absolute;
    left: 15px; top: 6px;
    width: 140px; height: 162px;
    background: linear-gradient(180deg, rgba(79,134,214,0.35), var(--art));
    clip-path: polygon(0 100%, 0 55%, 30% 55%, 35% 15%, 55% 0, 80% 0, 80% 100%);
  }
  .art-refinery {
    position: absolute;
    left: 665px; top: 64px;
    width: 175px; height: 106px;
    background: linear-gradient(180deg, rgba(79,134,214,0.35), var(--art));
    clip-path: polygon(0 100%, 0 60%, 20% 60%, 25% 10%, 45% 0, 60% 20%, 80% 30%, 100% 45%, 100% 100%);
  }
  .company-name {
    position: absolute;
    left: 0; right: 0; top: 44px;
    margin: 0;
    text-align: center;
    font-family: "Source Sans 3", sans-serif;
    font-weight: 700;
    font-size: 31px;
    color: var(--ink);
    letter-spacing: 0.2px;
  }
  .company-address {
    position: absolute;
    left: 0; right: 0; top: 92px;
    margin: 0;
    text-align: center;
    font-family: "Cabin", sans-serif;
    font-size: 17px;
    line-height: 22px;
    color: var(--ink);
    font-style: normal;
  }
  .company-reg {
    position: absolute;
    left: 0; right: 0; top: 143px;
    margin: 0;
    text-align: center;
    font-family: "Cabin", sans-serif;
    font-size: 11px;
    color: var(--ink);
  }
  .header-rule {
    position: absolute;
    left: 0; top: 177px;
    width: 840px; height: 2px;
    background: var(--rule);
  }
  .footer-band {
    position: absolute;
    left: 0; top: 1028px;
    width: 840px; height: 56px;
    background: var(--band);
    border-top: 2px solid var(--rule);
    box-sizing: border-box;
    display: flex;
    align-items: center;
    justify-content: center;
    gap: 18px;
    font-family: "Cabin", sans-serif;
    font-weight: 500;
    font-size: 17px;
    color: var(--ink);
  }
</style>
</head>
<body>
  <main class="letterhead">
    <header class="header-band">
      <div class="art-pumpjack" role="img" aria-label="Silhouette of an oil pump jack"></div>
      <h1 class="company-name">Hartwell Inspection Services Ltd</h1>
      <address class="company-address">The Willows, Mill Road, Ashby, Marlowe,<br>Kent TN4 8QX</address>
      <p class="company-reg">Reg. #4820516</p>
      <div class="art-refinery" role="img" aria-label="Silhouette of a refinery with smoking chimneys"></div>
    </header>
    <div class="header-rule"></div>
    <footer class="footer-band">
      <span class="footer-email">email: office@hartwellinspect.co.uk</span>
      <span class="footer-sep">•</span>
      <span class="footer-mobile">mobile: 07700 914382</span>
    </footer>
  </main>
</body>
</html>
```